Spa Business Card Design Project

Hello! We are a boutique spa for men and women that is rebranding. I would like a memorable new business card that showcases our beautiful new logo and our unique business. I would like it to be classic/timeless and eclectic/artistic at the  same time.
I am a fan of negative space as you can tell from the logo. I am also open to any creative ideas.
Multi sided design. Two sided design is acceptable as an option, too. "Flaps/folds/whatever the design term is" are optional- whether full vertical or horizontal, half flap, full flap etc
On either side next to the golden snail I would potentially like to see "Ease up. Savor Life."  Possibly on one statment on top of each other, crowned with the snail. Or the statment following the snail on one line... I am open for a creative suprise, too.
The back I would like room for the standard Information
"3817 Birch Lane
Ashgrove, Vermont 05741
(802) 462 3085
info@thecorvella spa.com
The snail is to be done in gold ink.
Can I also Have an option for cards that are individualized for staff members, too?

Updates
Project Deadline Extended
Reason: I apologize for the deadline extension. My day was more involved than anticipated in other matters. Hope to have this closed by next Tuesday.
Thank you

Target Market(s)
Men and women with expendable income between the ages of 30-55
Industry/Entity Type
Boutique
Requirements
Must have
- only black and gold ink.

Nice to have
- One of a kind.
Showcase the snail :-)
make you smile :-)
Fun, but professional.
Should not have
- Lots of color.
Too feminine.
Too busy.

```html
<!DOCTYPE html>
<html lang="en">
<head>
<meta charset="utf-8">
<title>The Corvella Spa – Business Cards</title>
<link rel="stylesheet" href="https://fonts.googleapis.com/css2?family=Jost:wght@400;500;600&display=swap">
<style>
  :root {
    --backdrop: #3b3b3b;
    --card-light: #fbfbfb;
    --card-edge: #d6d6d8;
    --ink-grey: #5a5a5c;
    --ink-soft: #8a8a8c;
    --gold: #d4ad62;
    --gold-deep: #c99f52;
  }
  * { box-sizing: border-box; margin: 0; padding: 0; }
  html, body { width: 1200px; height: 946px; overflow: hidden; }
  body {
    background: var(--backdrop);
    font-family: "Jost", sans-serif;
    position: relative;
  }
  .card {
    position: absolute;
    width: 555px;
    height: 318px;
    background: radial-gradient(ellipse at 50% 50%, var(--card-light) 0%, #f0f0f1 45%, var(--card-edge) 100%);
    overflow: hidden;
  }
  .card--front { left: 32px; top: 78px; }
  .card--back { left: 615px; top: 78px; }
  .card--staff { left: 337px; top: 467px; }

  .pattern-field {
    position: absolute; inset: 0;
    background: linear-gradient(135deg, #ececee 0%, #f7f7f8 55%, #e4e4e6 100%);
  }
  .gold-band {
    position: absolute; left: 0; right: 0; height: 21px;
    background: linear-gradient(90deg, var(--gold-deep), var(--gold), var(--gold-deep));
  }
  .gold-band--top { top: 15px; }
  .gold-band--bottom { top: 280px; }

  .brand { position: absolute; text-align: center; color: var(--ink-grey); }
  .brand__name { font-weight: 500; line-height: 1; letter-spacing: 0.02em; }
  .brand__tagline { font-weight: 400; }

  .card--front .brand { left: 152px; top: 92px; width: 250px; }
  .card--front .brand__name { font-size: 38px; }
  .card--front .brand__tagline { font-size: 11px; margin-top: 8px; }

  .slogan {
    position: absolute; right: 24px; top: 271px;
    color: var(--gold); font-weight: 600; font-size: 12.5px;
  }

  .contact {
    position: absolute; left: 0; right: 0; top: 120px;
    text-align: center; color: var(--ink-soft);
    font-style: normal; font-weight: 600; font-size: 11px; line-height: 1.35;
  }

  .person { position: absolute; left: 42px; top: 137px; }
  .person__name {
    color: var(--gold); font-size: 26px; line-height: 1;
    text-transform: uppercase; letter-spacing: 0.01em;
  }
  .person__first { font-weight: 600; }
  .person__last { font-weight: 400; }
  .person__role { color: var(--ink-soft); font-size: 12px; margin-top: 3px; }

  .card--staff .brand { left: 360px; top: 118px; width: 150px; }
  .card--staff .brand__name { font-size: 22px; }
  .card--staff .brand__tagline { font-size: 6.5px; margin-top: 5px; }
</style>
</head>
<body>

  <section class="card card--front" aria-label="Card front">
    <div class="pattern-field" role="img" aria-label="Faint repeating snail pattern across the card"></div>
    <div class="brand">
      <p class="brand__name">The Corvella Spa</p>
      <p class="brand__tagline">a boutique spa for Men &amp; Women</p>
    </div>
    <p class="slogan">Ease up. Savor Life</p>
  </section>

  <section class="card card--back" aria-label="Card back">
    <div class="gold-band gold-band--top" role="img" aria-label="Gold band of repeating snails"></div>
    <address class="contact">
      <p>(802) 462 3085</p>
      <p>info@thecorvella spa.com</p>
      <p>3817 Birch Lane ,Ashgrove, Vermont 05741</p>
    </address>
    <div class="gold-band gold-band--bottom" role="img" aria-label="Gold band of repeating snails"></div>
  </section>

  <section class="card card--staff" aria-label="Staff card">
    <div class="gold-band gold-band--top" role="img" aria-label="Gold band of repeating snails"></div>
    <div class="person">
      <p class="person__name"><span class="person__first">Mirela</span><span class="person__last">Dovan</span></p>
      <p class="person__role">occupation</p>
    </div>
    <div class="brand">
      <p class="brand__name">The Corvella Spa</p>
      <p class="brand__tagline">a boutique spa for Men &amp; Women</p>
    </div>
    <div class="gold-band gold-band--bottom" role="img" aria-label="Gold band of repeating snails"></div>
  </section>

</body>
</html>
```